Business Card Design
Brightvale Marks
Modern
Kemi Varo
47 Olumide Bankole Crescent
Wuse 2
Abuja
Nigeria
info@brightvalemarks.com
www.brightvalemarks.com

```html
<!DOCTYPE html>
<html lang="en">
<head>
<meta charset="utf-8">
<title>Brightvale Marks — Business Card</title>
<link rel="stylesheet" href="https://fonts.googleapis.com/css2?family=Cinzel:wght@400;600&display=swap">
<style>
  :root {
    --page-bg: #e9ebee;
    --card-white: #ffffff;
    --card-edge: #d9dcdf;
    --brand-blue: #1f78b4;
    --deep-blue: #0f5d94;
    --sky-blue: #4aa8dc;
    --brand-green: #7cbf2f;
    --leaf-green: #5aa324;
    --ink-grey: #5b6168;
    --soft-grey: #8a9096;
  }
  * { box-sizing: border-box; margin: 0; padding: 0; }
  html, body { width: 1200px; height: 980px; overflow: hidden; }
  body {
    background: var(--page-bg);
    font-family: "Cinzel", Georgia, serif;
    position: relative;
  }
  .card {
    position: absolute;
    width: 700px;
    height: 400px;
    background: var(--card-white);
    border-radius: 24px;
    overflow: hidden;
    box-shadow: 0 0 0 1px var(--card-edge), 0 14px 30px rgba(40, 50, 60, 0.12);
  }
  .card-back { left: 440px; top: 60px; }
  .card-front { left: 60px; top: 520px; }

  /* Brand lockup */
  .brand {
    display: flex;
    align-items: center;
    gap: 14px;
  }
  .brand-dot {
    width: 26px;
    height: 26px;
    border-radius: 50%;
    background: var(--brand-green);
    flex: none;
  }
  .brand-name {
    font-family: "Cinzel", Georgia, serif;
    font-weight: 600;
    color: var(--brand-blue);
    letter-spacing: 1px;
    text-transform: uppercase;
    white-space: nowrap;
  }

  /* Back */
  .card-back .brand {
    position: absolute;
    left: 0; right: 0; top: 150px;
    justify-content: center;
  }
  .card-back .brand-name { font-size: 30px; }
  .card-back .website {
    position: absolute;
    left: 0; right: 0; top: 230px;
    text-align: center;
    font-size: 13px;
    letter-spacing: 5px;
    color: var(--soft-grey);
    text-transform: uppercase;
  }

  /* Front */
  .contact-list {
    position: absolute;
    left: 34px;
    top: 30px;
    list-style: none;
  }
  .contact-list li {
    display: flex;
    align-items: center;
    gap: 9px;
    height: 22px;
    font-size: 13px;
    color: var(--ink-grey);
    letter-spacing: 0.4px;
    white-space: nowrap;
  }
  .contact-icon {
    width: 15px;
    height: 15px;
    flex: none;
  }
  .card-front .brand {
    position: absolute;
    left: 270px;
    top: 178px;
  }
  .card-front .brand-name { font-size: 26px; }
  .tagline {
    position: absolute;
    left: 310px;
    top: 214px;
    font-size: 10px;
    color: var(--leaf-green);
    letter-spacing: 1.5px;
    text-transform: uppercase;
    white-space: nowrap;
  }
  .front-waves {
    position: absolute;
    left: 0;
    top: 0;
    width: 700px;
    height: 400px;
  }
  .holder-name {
    position: absolute;
    right: 46px;
    bottom: 24px;
    font-size: 24px;
    color: var(--card-white);
    letter-spacing: 1px;
    white-space: nowrap;
  }
</style>
</head>
<body>

  <section class="card card-back" aria-label="Business card back">
    <div class="brand">
      <span class="brand-dot"></span>
      <span class="brand-name">Brightvale Marks</span>
    </div>
    <p class="website">www.brightvalemarks.com</p>
  </section>

  <section class="card card-front" aria-label="Business card front">
    <svg class="front-waves" viewBox="0 0 700 400" aria-hidden="true">
      <defs>
        <linearGradient id="band-blue" x1="0" y1="0" x2="1" y2="1">
          <stop offset="0" stop-color="#0f5d94"/>
          <stop offset="0.55" stop-color="#1f78b4"/>
          <stop offset="1" stop-color="#4aa8dc"/>
        </linearGradient>
        <linearGradient id="band-sheen" x1="0" y1="0" x2="1" y2="0">
          <stop offset="0" stop-color="#6fc0ea" stop-opacity="0.55"/>
          <stop offset="1" stop-color="#6fc0ea" stop-opacity="0"/>
        </linearGradient>
      </defs>
      <path d="M0 218 C180 270 420 318 700 302 L700 400 L0 400 Z" fill="url(#band-blue)"/>
      <path d="M0 232 C200 290 430 330 700 318 L700 332 C430 344 200 306 0 252 Z" fill="url(#band-sheen)"/>
      <path d="M0 196 C190 252 430 300 700 284" fill="none" stroke="#7cbf2f" stroke-width="7"/>
      <path d="M0 208 C190 262 430 306 700 292" fill="none" stroke="#b8dd8a" stroke-width="2"/>
    </svg>

    <ul class="contact-list">
      <li>
        <svg class="contact-icon" viewBox="0 0 16 16" aria-hidden="true"><path d="M8 1a5 5 0 0 0-5 5c0 4 5 9 5 9s5-5 5-9a5 5 0 0 0-5-5zm0 7a2 2 0 1 1 0-4 2 2 0 0 1 0 4z" fill="#1f78b4"/></svg>
        47 Olumide Bankole Crescent
      </li>
      <li>
        <svg class="contact-icon" viewBox="0 0 16 16" aria-hidden="true"><circle cx="8" cy="8" r="3" fill="#7cbf2f"/></svg>
        Lindel 4 Orwen Coast
      </li>
      <li>
        <svg class="contact-icon" viewBox="0 0 16 16" aria-hidden="true"><path d="M4 1.5l2.5 3-1.5 2c1 2 2.5 3.5 4.5 4.5l2-1.5 3 2.5-1.5 2.5C7 14 2 9 1.5 3z" fill="#1f78b4"/></svg>
        (+00) 810 555 0192
      </li>
      <li>
        <svg class="contact-icon" viewBox="0 0 16 16" aria-hidden="true"><rect x="1.5" y="3.5" width="13" height="9" rx="1" fill="none" stroke="#7cbf2f" stroke-width="1.6"/><path d="M2 4l6 5 6-5" fill="none" stroke="#7cbf2f" stroke-width="1.6"/></svg>
        info@brightvalemarks.com
      </li>
      <li>
        <svg class="contact-icon" viewBox="0 0 16 16" aria-hidden="true"><circle cx="8" cy="8" r="6.3" fill="none" stroke="#1f78b4" stroke-width="1.5"/><path d="M1.8 8h12.4M8 1.7c-3 3.5-3 9 0 12.6M8 1.7c3 3.5 3 9 0 12.6" fill="none" stroke="#1f78b4" stroke-width="1.2"/></svg>
        www.brightvalemarks.com
      </li>
    </ul>

    <div class="brand">
      <span class="brand-dot"></span>
      <span class="brand-name">Brightvale Marks</span>
    </div>
    <p class="tagline">Building Value With Every Mark</p>

    <p class="holder-name">Kemi Varo</p>
  </section>

</body>
</html>
```